Rising Paths Web Design

I am starting a new company that will provide LIFE COACHING services - I have tried to design a website, but it's too complicated. Right now, it's just me - I'm the only person that will provide services through the website - I have used artmarket to purchase a logo (see below). I want to be able to update the website myself, but need a template - basic design. Because I am not technologically savvy enough to explain in words - I basically want to have a website that will provide basic information about my services (coaching), a page about me and my background, hopefully scheduling possibilities, and testimonials — also a page for writing/blogs. I bought a website through NetHarbor - so when I have a template, I guess I”d use that - but maybe I’ll need to work with a designer to actually get it up on the internet. I have a head shot that I’ll upload, too.
Target Market(s)
Clients from the independent (private school) world - teachers, administrators
Number of Pages Required
4 page
Look and feel
Each slider illustrates characteristics of the customer's brand and the style your logo design should communicate.

```html
<!DOCTYPE html>
<html lang="en">
<head>
<meta charset="utf-8">
<title>Rising Paths Coaching</title>
<link href="https://fonts.googleapis.com/css2?family=Cinzel:wght@400;700&family=Montserrat:wght@300;400;600;700&family=Lato:ital,wght@0,400;0,700;1,400&display=swap" rel="stylesheet">
<style>
:root{
  --teal:#1fb3a1;
  --teal-dark:#149a8a;
  --teal-light:#5fcabc;
  --orange:#e9a010;
  --ink:#2a2a2a;
  --body:#4a4a4a;
  --muted:#8a8a8a;
  --line:#d9d9d9;
  --white:#ffffff;
}
*{box-sizing:border-box;margin:0;padding:0}
html,body{width:1200px;height:4594px;overflow:hidden;background:var(--white)}
body{position:relative;font-family:"Lato",sans-serif;color:var(--body)}
.abs{position:absolute}
.serif{font-family:"Cinzel",serif;color:var(--ink);font-weight:400;letter-spacing:1px}
.sans{font-family:"Montserrat",sans-serif}
.photo{position:absolute}

/* top bar + header */
.topbar{left:595px;top:0;width:605px;height:40px;background:var(--teal);clip-path:polygon(22px 0,100% 0,100% 100%,0 100%);
  display:flex;align-items:center;gap:34px;padding-left:50px;color:var(--white);font:400 12px "Montserrat",sans-serif}
.topbar b{font-weight:700}
.topbar span{display:flex;align-items:center;gap:7px}
.header{left:0;top:0;width:1200px;height:125px}
.brand-badge{left:86px;top:-8px;width:160px;height:160px;border-radius:50%;background:var(--white);box-shadow:0 2px 10px rgba(0,0,0,.08);
  display:flex;align-items:center;justify-content:center;z-index:3}
.brand-name{font:400 19px "Cinzel",serif;color:var(--ink);letter-spacing:.5px}
.nav{left:0;top:73px;width:1200px;font:500 14px "Montserrat",sans-serif;color:var(--ink)}
.nav a{position:absolute;text-decoration:none;color:var(--ink);transform:translateX(-50%);white-space:nowrap}
.nav a.active{font-weight:700}
.nav-underline{left:326px;top:120px;width:78px;height:3px;background:var(--teal)}
.btn-contact{left:970px;top:64px;width:135px;height:41px;border:2px solid var(--teal);border-radius:22px;color:var(--teal);
  font:600 12px "Montserrat",sans-serif;display:flex;align-items:center;justify-content:center}

/* hero */
.hero{left:0;top:125px;width:1200px;height:705px;overflow:hidden;
  background:linear-gradient(90deg,#f3f3f2 0%,#ecebe8 38%,#d9d6d0 60%,#cfcbc4 80%,#e0d8c8 100%)}
.hero-photo{left:470px;top:0;width:730px;height:705px;background:radial-gradient(ellipse at 40% 45%,#c8c4bd 0%,#d8d4cc 40%,rgba(230,228,224,0) 75%)}
.hero-welcome{left:0;width:610px;top:196px;text-align:center;font:300 25px "Montserrat",sans-serif;color:#666;letter-spacing:1px}
.hero-title{left:0;width:610px;top:235px;text-align:center;font-size:52px;line-height:56px}
.hero-title .accent{color:var(--teal)}
.btn-schedule{left:157px;top:362px;width:291px;height:58px;background:var(--orange);color:var(--white);
  font:700 14px "Montserrat",sans-serif;letter-spacing:1px;display:flex;align-items:center;justify-content:center}
.hero-arrow{left:588px;top:555px}

/* about */
.about-frame{left:140px;top:894px;width:394px;height:392px;border-top:5px solid var(--teal);border-right:5px solid var(--teal);border-radius:24px 0 0 0}
.about-photo{left:121px;top:912px;width:398px;height:378px;border-radius:40px 0 0 0;background:linear-gradient(135deg,#e6e7e9 0%,#d8d6d3 45%,#c9c0b8 75%,#b9aaa2 100%)}
.eyebrow{font:400 15px "Montserrat",sans-serif;color:var(--teal);letter-spacing:1px}
.about-eyebrow{left:593px;top:902px}
.about-title{left:592px;top:922px;font-size:40px}
.about-text{left:592px;width:480px;font:400 16.5px/27px "Lato",sans-serif;color:var(--body);text-align:justify}
.btn-outline{border:2px solid var(--teal);border-radius:30px;color:var(--teal);font:700 13px "Montserrat",sans-serif;letter-spacing:1.5px;display:flex;align-items:center;justify-content:center}
.about-btn{left:588px;top:1224px;width:180px;height:50px}

/* section headings */
.center{left:0;width:1200px;text-align:center}
.rule{left:566px;width:68px;height:2px;background:var(--teal)}

/* services */
.service{top:1519px;height:328px;overflow:hidden}
.service-label{position:absolute;left:0;right:0;bottom:16px;text-align:center;color:var(--white);font:700 17px "Montserrat",sans-serif;letter-spacing:.5px}
.service-feature{left:291px;top:1494px;width:315px;height:371px;background:linear-gradient(160deg,#22b8a6,#1aa999);border-radius:0 34px 0 0;color:var(--white);text-align:center;z-index:2}
.service-feature h3{font:700 21px/25px "Montserrat",sans-serif;margin-top:128px}
.service-feature p{font:400 14px/23px "Lato",sans-serif;opacity:.9;margin:10px 36px 0}
.feature-btn{margin:16px auto 0;width:138px;height:36px;background:var(--white);border-radius:20px;color:var(--teal);font:700 11px "Montserrat",sans-serif;letter-spacing:1px;display:flex;align-items:center;justify-content:center}

/* why choose */
.why{left:0;top:1847px;width:1200px;height:631px;overflow:hidden;
  background:linear-gradient(180deg,#cfe3e9 0%,#c5d7de 35%,#9db0b8 58%,#5f6f76 78%,#39444a 100%)}
.why-title{left:139px;top:145px;font-size:38px;line-height:40px;color:#333}
.why-title b{font-weight:700}
.why-text{left:139px;top:270px;width:440px;font:400 17px/27px "Lato",sans-serif;color:#333}
.why-btn{left:137px;top:408px;width:175px;height:46px;background:var(--teal);border-radius:24px;color:var(--white);font:600 14px "Montserrat",sans-serif;display:flex;align-items:center;justify-content:center}

/* blog */
.blog-photo{top:2675px;width:311px;height:215px;border-radius:0 30px 0 0}
.blog-card{top:2858px;width:280px;height:200px;background:var(--white);box-shadow:0 3px 14px rgba(0,0,0,.08);padding:22px 0 0 40px}
.blog-card.active{border-bottom:4px solid var(--teal)}
.blog-date{font:400 12px "Montserrat",sans-serif;color:var(--teal);display:flex;align-items:center;gap:5px}
.blog-title{font:700 14px/18px "Montserrat",sans-serif;color:var(--ink);margin-top:12px;width:190px}
.blog-text{font:400 11px/17px "Lato",sans-serif;color:var(--muted);margin-top:12px;width:215px}
.blog-btn{width:120px;height:30px;margin-top:14px;font-size:9px;letter-spacing:.5px;border-width:1.5px}

/* testimonials */
.testi{left:0;top:3147px;width:1200px;height:548px;background:linear-gradient(100deg,#4ec3b5 0%,#28b4a3 50%,#15a893 100%)}
.testi-eyebrow{top:68px;color:var(--white)}
.testi-title{top:96px;color:var(--white);font-size:40px}
.testi-rule{top:148px;background:var(--white)}
.testi-box{left:307px;top:169px;width:650px;height:265px;border:2px solid rgba(255,255,255,.85)}
.testi-photo{left:216px;top:188px;width:222px;height:222px;border-radius:50%;border:4px solid var(--white);background:radial-gradient(circle at 50% 40%,#e7c7b0 0%,#c98a66 55%,#8a6a55 100%)}
.testi-quote{left:460px;top:215px;width:480px;font:italic 400 19px/34px "Lato",sans-serif;color:var(--white)}
.testi-name{left:460px;top:343px;font:700 16px "Montserrat",sans-serif;color:var(--white);letter-spacing:.5px}
.testi-mark{left:848px;top:330px;font:700 110px/1 "Cinzel",serif;color:var(--white)}

/* appointment */
.book{left:0;top:3695px;width:1200px;height:740px;overflow:hidden;
  background:linear-gradient(180deg,#f3d9a8 0%,#e9b779 25%,#b98a5a 55%,#6d6147 80%,#55513f 100%)}
.book-card{left:565px;top:3803px;width:526px;height:378px;background:rgba(255,255,255,.96);border-radius:0 60px 0 0}
.book-eyebrow{left:41px;top:38px;font-size:12px}
.book-title{left:41px;top:58px;font-size:25px}
.field{position:absolute;height:40px;border:1px solid #c9c9c9;background:var(--white);font:400 12px "Lato",sans-serif;color:#777;padding:0 14px;display:flex;align-items:center;gap:5px}
.field.area{height:79px;align-items:flex-start;padding-top:12px}
.book-btn{left:41px;top:309px;width:168px;height:45px;background:var(--teal);border-radius:24px;color:var(--white);font:700 13px "Montserrat",sans-serif;letter-spacing:1.5px;display:flex;align-items:center;justify-content:center}

/* footer */
.footer-badge{left:531px;top:4260px;width:150px;height:150px;border-radius:50%;background:var(--white);display:flex;align-items:center;justify-content:center;z-index:3}
.footer-nav{top:4436px;font:500 14px "Montserrat",sans-serif;color:var(--ink)}
.footer-nav span{position:absolute;transform:translateX(-50%);white-space:nowrap}
.copy{top:4474px;font:400 11px "Montserrat",sans-serif;color:var(--muted)}
.social{top:4508px;width:36px;height:36px;border-radius:50%;background:var(--teal)}
</style>
</head>
<body>

<!-- header -->
<div class="abs topbar">
  <span><svg width="16" height="16" viewBox="0 0 24 24" fill="none" stroke="#fff" stroke-width="2"><path d="M5 3h4l2 5-3 2a12 12 0 0 0 6 6l2-3 5 2v4a2 2 0 0 1-2 2A17 17 0 0 1 3 5a2 2 0 0 1 2-2z"/></svg>Call Us: <b>+100 555 0142</b></span>
  <span><svg width="18" height="14" viewBox="0 0 24 18" fill="#fff"><path d="M0 0h24v18H0z" fill-opacity=".95"/><path d="M1 1l11 9 11-9" stroke="#1fb3a1" stroke-width="2" fill="none"/></svg>Email: <b>hello@risingpaths.co</b></span>
</div>
<div class="abs brand-badge"><span class="brand-name">RISING PATHS</span></div>
<nav class="abs nav">
  <a class="active" style="left:362px">HOME</a>
  <a style="left:481px">ABOUT US</a>
  <a style="left:612px">SERVICES</a>
  <a style="left:731px">BLOGS</a>
  <a style="left:868px">TESTIMONIALS</a>
</nav>
<div class="abs nav-underline"></div>
<div class="abs btn-contact">CONTACT US</div>

<!-- hero -->
<section class="abs hero">
  <div class="photo hero-photo" role="img" aria-label="Smiling coach in conversation with a client in a bright office"></div>
  <div class="abs hero-welcome">WELCOME TO</div>
  <h1 class="abs serif hero-title">RISING PATHS<br><span class="accent">COACHING</span></h1>
  <div class="abs btn-schedule">SCHEDULE APPOINTMENT</div>
  <svg class="abs hero-arrow" width="16" height="30" viewBox="0 0 16 30" fill="none" stroke="#fff" stroke-width="2"><path d="M8 0v28M1 21l7 7 7-7"/></svg>
  <svg class="abs" style="left:0;top:600px" width="1200" height="105" viewBox="0 0 1200 105">
    <path d="M0 105 C300 30 800 20 1200 105 L1200 105 L0 105Z" fill="#fff"/>
    <path d="M0 100 C300 25 800 15 1200 100" stroke="#1fb3a1" stroke-width="4" fill="none"/>
  </svg>
</section>

<!-- about -->
<div class="abs about-frame"></div>
<div class="photo about-photo" role="img" aria-label="Head shot of the coach, a smiling woman with short silver hair"></div>
<div class="abs eyebrow about-eyebrow">WHO I AM</div>
<h2 class="abs serif about-title">ABOUT <b>ME</b></h2>
<p class="abs about-text" style="top:998px">Lorem ipsum dolor sit amet, consectetur adipiscing elit, sed do eiusmod tempor incididunt ut labore et dolore magna aliqua. Ut enim ad minim veniam, quis nostrud exercitation ullamco laboris nisi ut aliquip ex e</p>
<p class="abs about-text" style="top:1136px">Duis aute irure dolor in reprehenderit in voluptate velit esse cillum dolore eu fugiat nulla pariatur.</p>
<div class="abs btn-outline about-btn">LEARN MORE</div>

<!-- services -->
<div class="abs eyebrow center" style="top:1372px">WHAT WE OFFER</div>
<h2 class="abs serif center" style="top:1393px;font-size:36px">COACHING <b>SERVICE</b></h2>
<div class="abs rule" style="top:1443px"></div>

<div class="abs service" style="left:0;width:291px;background:linear-gradient(160deg,#a0584a 0%,#c9a38f 40%,#cfd7de 100%)" role="img" aria-label="Woman smiling in a relaxed coaching session">
  <div class="service-label">LIFE COACHING</div>
</div>
<div class="abs service-feature">
  <svg style="position:absolute;left:132px;top:62px" width="48" height="48" viewBox="0 0 48 48" fill="none" stroke="#fff" stroke-width="2"><circle cx="16" cy="14" r="5"/><circle cx="32" cy="12" r="5"/><path d="M8 40V26a8 8 0 0 1 16 0v14M24 40V24a8 8 0 0 1 16 0v16"/></svg>
  <h3>COACHING &amp;<br>MENTORING</h3>
  <p>Lorem ipsum dolor sit amet consectetur adipiscing elit, sed do eiusmod tempor.</p>
  <div class="feature-btn">LEARN MORE</div>
</div>
<div class="abs service" style="left:606px;width:296px;background:linear-gradient(180deg,#7fa7c0 0%,#e0a860 45%,#8a6a4c 70%,#5c5148 100%)" role="img" aria-label="Wooden boardwalk leading to the sea at sunset">
  <div class="service-label">LIFE COACHING</div>
</div>
<div class="abs service" style="left:909px;width:291px;background:linear-gradient(160deg,#e9e3da 0%,#c9b7a8 50%,#8c6d5f 100%)" role="img" aria-label="Woman taking notes during a coaching session">
  <div class="service-label">LIFE COACHING</div>
</div>

<!-- why choose -->
<section class="abs why" role="img" aria-label="Hiker with raised arm on a mountain summit above misty ranges">
  <h2 class="abs serif why-title">WHY CHOOSE<br><b>RISING PATHS</b></h2>
  <p class="abs why-text">Lorem ipsum dolor sit amet, consectetur adipiscing elit, sed do eiusmod tempor incididunt ut labore et dolore magna aliqua. Ut enim ad minim veniam, quis nostrud exercitation ullamco laboris nisi ut</p>
  <div class="abs why-btn">LEARN MORE</div>
</section>

<!-- blogs -->
<div class="abs eyebrow center" style="top:2560px;font-size:17px">RECENT POSTS</div>
<h2 class="abs serif center" style="top:2580px;font-size:38px">LATEST BLOGS</h2>

<div class="photo blog-photo" style="left:114px;background:linear-gradient(135deg,#cfd3d6,#6b4a3e 55%,#d8d3cf)" role="img" aria-label="Two women talking at a table"></div>
<div class="photo blog-photo" style="left:449px;background:linear-gradient(135deg,#d9dde0,#b9b4ad 50%,#e8e6e2)" role="img" aria-label="Woman smiling in a bright meeting room"></div>
<div class="photo blog-photo" style="left:781px;background:linear-gradient(135deg,#e8d9c0,#c98a4c 50%,#8a6a3a)" role="img" aria-label="Woman in a hat outdoors at golden hour"></div>

<div class="abs blog-card active" style="left:130px">
  <div class="blog-date"><svg width="12" height="12" viewBox="0 0 12 12" fill="none" stroke="#1fb3a1"><rect x=".5" y="1.5" width="11" height="10"/><path d="M.5 4.5h11M3 0v3M9 0v3"/></svg>02 June 2022</div>
  <div class="blog-title">Lorem Ipsum is simply dummy text</div>
  <div class="blog-text">Lorem Ipsum is simply dummy text of the printing and typesetting industry.</div>
  <div class="btn-outline blog-btn">LEARN MORE</div>
</div>
<div class="abs blog-card" style="left:465px">
  <div class="blog-date"><svg width="12" height="12" viewBox="0 0 12 12" fill="none" stroke="#1fb3a1"><rect x=".5" y="1.5" width="11" height="10"/><path d="M.5 4.5h11M3 0v3M9 0v3"/></svg>04 June 2022</div>
  <div class="blog-title">Lorem Ipsum is simply dummy text</div>
  <div class="blog-text">Lorem Ipsum is simply dummy text of the printing and typesetting industry.</div>
  <div class="btn-outline blog-btn">LEARN MORE</div>
</div>
<div class="abs blog-card" style="left:797px">
  <div class="blog-date"><svg width="12" height="12" viewBox="0 0 12 12" fill="none" stroke="#1fb3a1"><rect x=".5" y="1.5" width="11" height="10"/><path d="M.5 4.5h11M3 0v3M9 0v3"/></svg>05 June 2022</div>
  <div class="blog-title">Lorem Ipsum is simply dummy text</div>
  <div class="blog-text">Lorem Ipsum is simply dummy text of the printing and typesetting industry.</div>
  <div class="btn-outline blog-btn">LEARN MORE</div>
</div>

<!-- testimonials -->
<section class="abs testi">
  <div class="abs eyebrow center testi-eyebrow">WHAT PEOPLE SAY</div>
  <h2 class="abs serif center testi-title">TESTIMONIALS</h2>
  <div class="abs rule testi-rule"></div>
  <div class="abs testi-box"></div>
  <div class="abs testi-photo" role="img" aria-label="Portrait of a smiling client with red hair"></div>
  <p class="abs testi-quote">Morbi diam mauris viverra in gravida eu mattis in ante Morbi eget arcu Morbi porta libero id ullamcorper non-ummy nibh ligula pulvinar metus eget consectet</p>
  <div class="abs testi-name">LENA HARTWELL</div>
  <div class="abs testi-mark">”</div>
  <svg class="abs" style="left:86px;top:272px" width="24" height="44" viewBox="0 0 24 44" fill="none" stroke="#fff" stroke-width="3"><path d="M22 2L3 22l19 20"/></svg>
  <svg class="abs" style="left:1072px;top:272px" width="24" height="44" viewBox="0 0 24 44" fill="none" stroke="#fff" stroke-width="3"><path d="M2 2l19 20L2 42"/></svg>
</section>

<!-- appointment -->
<section class="abs book" role="img" aria-label="Woman sitting on a rock overlooking mountains at sunset">
  <svg class="abs" style="left:0;top:600px" width="1200" height="140" viewBox="0 0 1200 140">
    <path d="M0 140 L0 115 C250 50 950 50 1200 115 L1200 140Z" fill="#fff"/>
    <path d="M0 112 C250 47 950 47 1200 112" stroke="#1fb3a1" stroke-width="4" fill="none"/>
  </svg>
</section>
<div class="abs book-card">
  <div class="abs eyebrow book-eyebrow">BOOK APPOINTMENT NOW</div>
  <h2 class="abs serif book-title">SCHEDULE AN APPOINTMENT</h2>
  <div class="field" style="left:41px;top:118px;width:211px">Name</div>
  <div class="field" style="left:259px;top:118px;width:212px">Email address</div>
  <div class="field" style="left:41px;top:166px;width:211px">Phone</div>
  <div class="field" style="left:259px;top:166px;width:212px"><svg width="12" height="12" viewBox="0 0 12 12" fill="none" stroke="#1fb3a1"><rect x=".5" y="1.5" width="11" height="10"/><path d="M.5 4.5h11M3 0v3M9 0v3"/></svg>Select Date</div>
  <div class="field area" style="left:41px;top:214px;width:430px">Message</div>
  <div class="abs book-btn">BOOK NOW</div>
</div>

<!-- footer -->
<div class="abs footer-badge"><span class="brand-name" style="font-size:17px">RISING PATHS</span></div>
<div class="abs center footer-nav" style="height:20px">
  <span style="left:262px">HOME</span>
  <span style="left:382px">ABOUT US</span>
  <span style="left:513px">SERVICES</span>
  <span style="left:633px">BLOGS</span>
  <span style="left:771px">TESTIMONIALS</span>
  <span style="left:941px">CONTACT US</span>
</div>
<div class="abs center copy">© 2022 Rising Paths Coaching All Rights Reserved</div>
<div class="abs social" style="left:528px"></div>
<div class="abs social" style="left:572px"></div>
<div class="abs social" style="left:615px"></div>
<div class="abs social" style="left:660px"></div>

</body>
</html>
```